Marvane Painting Epoxy Flyer

We need a promotional flyer for a new epoxy floor coatings division of our painting company. We do epoxy garage floor coatings and paver sealing. It needs to be based on and very similar to the attached flyer. The garage floor picture needs to look more realistic, and the before and after pavers pictures should look less shiny but still a good contrast. Include attached logo

```html
<!DOCTYPE html>
<html lang="en">
<head>
<meta charset="utf-8">
<title>Marvane Painting Epoxy Flyer</title>
<link rel="stylesheet" href="https://fonts.googleapis.com/css2?family=Oswald:wght@500;700&family=Montserrat:ital,wght@0,800;1,400;1,600;1,700&family=Roboto+Condensed:wght@400;700&display=swap">
<style>
  :root {
    --blue: #0b3a98;
    --green: #4a7f35;
    --ink: #111111;
    --grey-line: #8a8a8a;
    --rule: #d9d9d9;
    --paper: #ffffff;
  }
  html, body { margin: 0; padding: 0; width: 967px; height: 1200px; overflow: hidden; background: var(--paper); }
  .flyer { position: relative; width: 967px; height: 1200px; background: var(--paper); font-family: "Roboto Condensed", sans-serif; color: var(--ink); }
  .abs { position: absolute; }
  .hr { position: absolute; height: 1px; background: var(--grey-line); }

  /* brand */
  .brand-mark { left: 0; width: 967px; top: 98px; height: 44px; display: flex; align-items: center; justify-content: center; gap: 12px; }
  .brand-dot { width: 26px; height: 26px; border-radius: 50%; background: var(--green); }
  .brand-name { font-family: "Roboto Condensed", sans-serif; font-weight: 700; font-size: 30px; color: var(--ink); text-transform: uppercase; letter-spacing: .5px; }
  .division { left: 0; width: 967px; top: 238px; text-align: center; font-family: "Montserrat", sans-serif; font-weight: 800; font-size: 21px; letter-spacing: 6px; color: var(--ink); }

  /* photos */
  .photo { position: absolute; }
  .garage-before { left: 77px; top: 269px; width: 529px; height: 386px; clip-path: polygon(0 0, 320px 0, 250px 100%, 0 100%);
    background: linear-gradient(160deg, #d9d9d6 0%, #a3a19b 22%, #77766f 55%, #605f59 100%); }
  .garage-after { left: 77px; top: 269px; width: 529px; height: 386px; clip-path: polygon(326px 0, 100% 0, 100% 100%, 256px 100%);
    background: linear-gradient(170deg, #e8e2d6 0%, #c9c7c2 18%, #9a9a9a 40%, #6a6a6a 75%, #4a4a4a 100%); }
  .pavers-before { left: 614px; top: 269px; width: 276px; height: 195px; background: linear-gradient(175deg, #8a7257 0%, #8a7257 16%, #9a7b5c 22%, #7f664d 60%, #6f5a45 100%); }
  .pavers-after { left: 614px; top: 472px; width: 276px; height: 183px; background: linear-gradient(175deg, #7a5f44 0%, #7a5f44 20%, #8b6448 26%, #7a563d 60%, #6a4a34 100%); }

  .tag { position: absolute; height: 39px; color: #fff; font-family: "Oswald", sans-serif; font-weight: 500; font-size: 23px; display: flex; align-items: center; justify-content: center; }
  .tag-before { background: #141414; }
  .tag-after { background: var(--blue); }

  /* headline */
  .headline { left: 77px; width: 813px; top: 652px; margin: 0; text-align: center; font-family: "Oswald", sans-serif; font-weight: 700; font-size: 66px; line-height: 80px; letter-spacing: -0.5px; white-space: nowrap; }
  .headline .amp { color: var(--blue); }
  .sub-rule { left: 283px; width: 401px; top: 732px; height: 2px; background: var(--blue); }
  .subhead { left: 0; width: 967px; top: 734px; text-align: center; font-family: "Montserrat", sans-serif; font-style: italic; font-size: 22px; letter-spacing: .5px; }

  /* service columns */
  .col-head { position: absolute; top: 767px; height: 35px; color: #fff; font-family: "Oswald", sans-serif; font-weight: 500; font-size: 24px; letter-spacing: .5px; display: flex; align-items: center; justify-content: center; }
  .col-epoxy { left: 77px; width: 411px; background: var(--blue); clip-path: polygon(0 0, 100% 0, 98.5% 100%, 0 100%); }
  .col-paver { left: 490px; width: 400px; background: var(--green); clip-path: polygon(1.5% 0, 100% 0, 100% 100%, 0 100%); }
  .col-divider { left: 0; top: 0; }

  .benefits { position: absolute; top: 805px; margin: 0; padding: 0; list-style: none; }
  .benefits li { position: relative; height: 36px; display: flex; align-items: center; font-size: 19.5px; border-bottom: 1px solid var(--rule); }
  .benefits li:last-child { border-bottom: none; }
  .benefits svg { position: absolute; left: -70px; top: 4px; }
  .benefits-epoxy { left: 157px; width: 400px; }
  .benefits-paver { left: 553px; width: 332px; }
  .benefits-epoxy li { width: 400px; } .benefits-epoxy li { border-bottom-color: var(--rule); }

  .band { left: 77px; width: 813px; top: 954px; height: 36px; background: var(--blue); color: #fff; display: flex; align-items: center; justify-content: center; font-family: "Montserrat", sans-serif; font-style: italic; font-weight: 700; font-size: 19px; letter-spacing: .3px; }

  /* trust points */
  .trust { position: absolute; top: 1005px; width: 200px; text-align: center; font-size: 17px; line-height: 19px; }
  .trust svg { display: block; margin: 0 auto 4px; }
  .trust-licensed { left: 132px; }
  .trust-family { left: 372px; }
  .trust-area { left: 628px; }
  .vdiv { position: absolute; top: 1003px; width: 1px; height: 55px; background: #c8c8c8; }

  /* call to action */
  .cta { left: 0; width: 967px; top: 1076px; text-align: center; color: var(--blue); font-family: "Roboto Condensed", sans-serif; font-weight: 700; font-size: 26px; letter-spacing: 2px; }
  .phone { left: 0; width: 967px; top: 1093px; text-align: center; font-family: "Montserrat", sans-serif; font-weight: 800; font-size: 57px; line-height: 70px; letter-spacing: 3px; color: var(--ink); }
  .promise { left: 0; width: 967px; top: 1153px; text-align: center; font-family: "Montserrat", sans-serif; font-style: italic; font-size: 15px; letter-spacing: 1px; }
  .blue-line { position: absolute; height: 1px; background: var(--blue); }
</style>
</head>
<body>
<div class="flyer">

  <header>
    <div class="hr" style="left:102px; width:194px; top:120px;"></div>
    <div class="hr" style="left:669px; width:196px; top:120px;"></div>
    <div class="abs brand-mark"><span class="brand-dot"></span><span class="brand-name">Marvane Painting</span></div>
    <div class="hr" style="left:323px; width:81px; top:252px; background:#333;"></div>
    <div class="hr" style="left:564px; width:80px; top:252px; background:#333;"></div>
    <div class="abs division">EPOXY</div>
  </header>

  <section class="gallery">
    <div class="photo garage-before" role="img" aria-label="Before: stained, cracked concrete garage floor"></div>
    <div class="photo garage-after" role="img" aria-label="After: speckled grey flake epoxy garage floor"></div>
    <div class="tag tag-before" style="left:77px; top:269px; width:122px; clip-path:polygon(0 0,100% 0,94% 100%,0 100%);">BEFORE</div>
    <div class="tag tag-after" style="left:403px; top:269px; width:135px; clip-path:polygon(4% 0,100% 0,100% 100%,0 100%);">AFTER</div>

    <div class="photo pavers-before" role="img" aria-label="Before: faded, weathered paver patio by a wood fence"></div>
    <div class="photo pavers-after" role="img" aria-label="After: sealed paver patio with restored colour"></div>
    <div class="tag tag-before" style="left:770px; top:269px; width:120px; clip-path:polygon(8% 0,100% 0,100% 100%,0 100%);">BEFORE</div>
    <div class="tag tag-after" style="left:762px; top:472px; width:128px; clip-path:polygon(8% 0,100% 0,100% 100%,0 100%);">AFTER</div>
  </section>

  <h1 class="abs headline">Ugrade Your Garage <span class="amp">&amp;</span> Driveway</h1>
  <div class="abs sub-rule"></div>
  <div class="abs subhead">From worn-out to like new</div>

  <section class="services">
    <div class="col-head col-epoxy">EPOXY FLOOR COATINGS</div>
    <div class="col-head col-paver">PAVER SEALING</div>
    <svg class="abs" style="left:460px; top:802px;" width="30" height="150" viewBox="0 0 30 150"><line x1="28" y1="0" x2="2" y2="150" stroke="#c8c8c8" stroke-width="1"/></svg>

    <ul class="benefits benefits-epoxy">
      <li><svg width="58" height="30" viewBox="0 0 58 30"><path d="M2 26 L40 18 L56 22 L18 30 Z" fill="#9aa0a6"/><path d="M24 20 L26 11" stroke="#6d747b" stroke-width="3"/><rect x="22" y="4" width="26" height="7" rx="3.5" fill="#1f56b8" transform="rotate(-12 35 8)"/></svg>Durable, long-lasting finish</li>
      <li><svg width="58" height="30" viewBox="0 0 58 30"><path d="M2 26 L40 18 L56 22 L18 30 Z" fill="#9aa0a6"/><path d="M24 20 L26 11" stroke="#6d747b" stroke-width="3"/><rect x="22" y="4" width="26" height="7" rx="3.5" fill="#1f56b8" transform="rotate(-12 35 8)"/></svg>Slip-resistant texture</li>
      <li><svg width="58" height="30" viewBox="0 0 58 30"><path d="M2 26 L40 18 L56 22 L18 30 Z" fill="#9aa0a6"/><path d="M24 20 L26 11" stroke="#6d747b" stroke-width="3"/><rect x="22" y="4" width="26" height="7" rx="3.5" fill="#1f56b8" transform="rotate(-12 35 8)"/></svg>Covers cracks &amp; imperfections</li>
      <li><svg width="58" height="30" viewBox="0 0 58 30"><path d="M2 26 L40 18 L56 22 L18 30 Z" fill="#9aa0a6"/><path d="M24 20 L26 11" stroke="#6d747b" stroke-width="3"/><rect x="22" y="4" width="26" height="7" rx="3.5" fill="#1f56b8" transform="rotate(-12 35 8)"/></svg>Easy to clean &amp; maintain</li>
    </ul>

    <ul class="benefits benefits-paver">
      <li><svg width="58" height="30" viewBox="0 0 58 30"><path d="M2 26 L40 18 L56 22 L18 30 Z" fill="#9aa0a6"/><path d="M24 20 L26 11" stroke="#6d747b" stroke-width="3"/><rect x="22" y="4" width="26" height="7" rx="3.5" fill="#1f56b8" transform="rotate(-12 35 8)"/></svg>Restores color &amp; enhances appearance</li>
      <li><svg width="58" height="30" viewBox="0 0 58 30"><path d="M2 26 L40 18 L56 22 L18 30 Z" fill="#9aa0a6"/><path d="M24 20 L26 11" stroke="#6d747b" stroke-width="3"/><rect x="22" y="4" width="26" height="7" rx="3.5" fill="#1f56b8" transform="rotate(-12 35 8)"/></svg>Protects from sun fading</li>
      <li><svg width="58" height="30" viewBox="0 0 58 30"><path d="M2 26 L40 18 L56 22 L18 30 Z" fill="#9aa0a6"/><path d="M24 20 L26 11" stroke="#6d747b" stroke-width="3"/><rect x="22" y="4" width="26" height="7" rx="3.5" fill="#1f56b8" transform="rotate(-12 35 8)"/></svg>Helps prevent weeds &amp; sand loss</li>
      <li><svg width="58" height="30" viewBox="0 0 58 30"><path d="M2 26 L40 18 L56 22 L18 30 Z" fill="#9aa0a6"/><path d="M24 20 L26 11" stroke="#6d747b" stroke-width="3"/><rect x="22" y="4" width="26" height="7" rx="3.5" fill="#1f56b8" transform="rotate(-12 35 8)"/></svg>Easier to clean &amp; maintain</li>
    </ul>
  </section>

  <div class="abs band">Practical upgrades that protect and improve your home</div>

  <section class="trust-points">
    <div class="trust trust-licensed">
      <svg width="30" height="34" viewBox="0 0 30 34"><path d="M15 1 L28 6 V16 C28 24 22 30 15 33 C8 30 2 24 2 16 V6 Z" fill="var(--blue)"/><path d="M15 6 L23 9 V16 C23 21 19 25 15 27 C11 25 7 21 7 16 V9 Z" fill="#fff"/><path d="M15 9 L20 11 V16 C20 19 18 22 15 23 Z" fill="var(--blue)"/></svg>
      Licensed &amp; Insured
    </div>
    <div class="vdiv" style="left:350px;"></div>
    <div class="trust trust-family" style="top:1000px;">
      <svg width="34" height="32" viewBox="0 0 34 32"><path d="M5 28 L27 6" stroke="var(--green)" stroke-width="4" stroke-linecap="round"/><path d="M29 28 L9 8" stroke="var(--green)" stroke-width="4" stroke-linecap="round"/><circle cx="7" cy="6" r="5" fill="none" stroke="var(--green)" stroke-width="3"/><rect x="24" y="2" width="8" height="6" fill="var(--green)" transform="rotate(45 28 5)"/></svg>
      Family-Owned<br>Local Business
    </div>
    <div class="vdiv" style="left:608px;"></div>
    <div class="trust trust-area" style="top:1000px;">
      <svg width="24" height="32" viewBox="0 0 24 32"><path d="M12 1 C5.5 1 1 6 1 12 C1 20 12 31 12 31 C12 31 23 20 23 12 C23 6 18.5 1 12 1 Z" fill="var(--blue)"/><circle cx="12" cy="12" r="4" fill="#fff"/></svg>
      Serving Prescott &amp;<br>Surrounding Areas
    </div>
  </section>

  <footer>
    <div class="blue-line" style="left:143px; width:155px; top:1092px;"></div>
    <div class="blue-line" style="left:669px; width:152px; top:1092px;"></div>
    <div class="abs cta">CALL FOR A FREE ESTIMATE</div>
    <div class="abs phone">928-555-0147</div>
    <div class="blue-line" style="left:143px; width:155px; top:1163px;"></div>
    <div class="blue-line" style="left:669px; width:152px; top:1163px;"></div>
    <div class="abs promise">Fast, professional service you can trust</div>
  </footer>

</div>
</body>
</html>
```